Torvane PT Business Card

I need the card to be bright/bold colours to stand out amongst others.
It needs to have my company logo.
I was not interested in pictures etc just a layout that attracts attention.

I have attached my old design which is very plain. I also needed change the contact details. And my description changed to Personal Trainer
Phone 0427391058
Facebook Torvane PT
No email address please, no street address.
And only Torvane PT (Please remove anything to do with Torvane Supplements)

```html
<!DOCTYPE html>
<html lang="en">
<head>
<meta charset="utf-8">
<title>Torvane PT Business Card</title>
<link rel="stylesheet" href="https://fonts.googleapis.com/css2?family=Open+Sans:wght@400;600;700;800&display=swap">
<style>
  :root {
    --brand-blue: #0A87CB;
    --name-blue: #2B4FA8;
    --brand-yellow: #F7D81A;
    --soft-yellow: #FFF5C9;
    --ink: #3A3A3A;
    --band-black: #1F1F1F;
    --paper: #FFFFFF;
    --backdrop: #F2F2F2;
  }
  * { box-sizing: border-box; margin: 0; padding: 0; }
  html, body {
    width: 1200px; height: 1200px; overflow: hidden;
    background: var(--backdrop);
    font-family: "Open Sans", sans-serif;
  }
  .sheet {
    width: 1200px; height: 1200px;
    display: flex; flex-direction: column; align-items: center; justify-content: center;
    gap: 56px;
  }
  .card {
    position: relative;
    width: 880px; height: 503px;
    overflow: hidden;
    box-shadow: 0 6px 18px rgba(0,0,0,0.12);
  }

  .wordmark {
    font-family: "Open Sans", sans-serif;
    font-weight: 800;
    letter-spacing: 2px;
    line-height: 1;
    white-space: nowrap;
  }
  .rule { position: absolute; height: 2px; }

  /* Front */
  .card-front { background: var(--brand-blue); }
  .card-front .wordmark {
    position: absolute; left: 0; right: 0; top: 190px; text-align: center;
    color: var(--paper); font-size: 96px;
  }
  .card-front .rule { left: 150px; right: 150px; top: 310px; background: var(--paper); }

  /* Back */
  .card-back { background: var(--paper); }
  .card-back .decor { position: absolute; left: 0; top: 0; }
  .card-back .wordmark {
    position: absolute; right: 64px; top: 70px;
    color: var(--brand-yellow); font-size: 88px;
  }
  .card-back .rule { right: 64px; width: 560px; top: 176px; background: var(--brand-blue); }

  .holder {
    position: absolute; right: 78px; top: 222px; text-align right;
    text-align: right;
    color: var(--name-blue);
  }
  .holder-name { font-size: 44px; font-weight: 700; line-height: 1.05; }
  .holder-role { font-size: 15px; font-weight: 600; letter-spacing: 0.5px; margin-top: 4px; }

  .contact {
    position: absolute; left: 150px; bottom: 100px;
    color: var(--ink);
    display: flex; align-items: center; gap: 16px;
  }
  .contact svg { flex: none; }
  .contact-phone { font-size: 42px; font-weight: 800; letter-spacing: 1px; }

  .dark-band {
    position: absolute; left: 0; bottom: 0;
    width: 680px; height: 58px;
    background: var(--band-black);
  }
  .social-tab {
    position: absolute; right: 0; bottom: 0;
    width: 250px; height: 98px;
    background: var(--brand-blue); color: var(--paper);
    border-top-left-radius: 30px;
    display: flex; align-items: center; justify-content: center; gap: 12px;
    font-size: 24px; font-weight: 400;
  }
  .social-dot { width: 26px; height: 26px; border-radius: 50%; background: var(--paper); }
</style>
</head>
<body>
<main class="sheet">
  <section class="card card-front" aria-label="Card front">
    <div class="wordmark">TORVANE PT</div>
    <div class="rule"></div>
  </section>

  <section class="card card-back" aria-label="Card back">
    <svg class="decor" width="880" height="503" viewBox="0 0 880 503" role="img" aria-label="Soft pale yellow curved accent">
      <defs>
        <radialGradient id="accentGlow" cx="0.3" cy="0.75" r="0.7">
          <stop offset="0" stop-color="#FFF5C9"/>
          <stop offset="0.7" stop-color="#FFF5C9"/>
          <stop offset="1" stop-color="#FFF5C9" stop-opacity="0"/>
        </radialGradient>
      </defs>
      <ellipse cx="300" cy="420" rx="300" ry="210" fill="url(#accentGlow)"/>
    </svg>

    <div class="wordmark">TORVANE PT</div>
    <div class="rule"></div>

    <div class="holder">
      <div class="holder-name">Dana Mercer</div>
      <div class="holder-role">PERSONAL TRAINER</div>
    </div>

    <div class="contact">
      <svg width="36" height="36" viewBox="0 0 34 34" aria-hidden="true">
        <circle cx="17" cy="17" r="15" fill="none" stroke="#0A87CB" stroke-width="3"/>
        <path d="M11 10c1-1 2-1 3 0l2 3c.5 1 0 2-1 2.5 1 2.5 2.5 4 5 5 .5-1 1.5-1.5 2.5-1l3 2c1 1 1 2 0 3-2 2-5 2-8 0-3-2-5-4-7-7-2-3-2-6 .5-7.5z" fill="#0A87CB"/>
      </svg>
      <span class="contact-phone">0427 391 058</span>
    </div>

    <div class="dark-band" aria-hidden="true"></div>

    <div class="social-tab">
      <span class="social-dot" aria-hidden="true"></span>
      <span>Torvane PT</span>
    </div>
  </section>
</main>
</body>
</html>
```